Flyer for an IT consultancy firm

We are an IT consultancy firm based in Iceland. We have a website at: www.brimvolt.com where you can get acquainted with our activities.
We require a double-sided flyer in A4 format to be handed out in conferences, trade shows etc. The flyer is basically a summarized overview of our range of services.

The deliverable should incorporate some visual elements that are relevant to our line of business such as:
• computers
• cybersecurity
• networks
Also, it would be nice to have visuals relating to Icelandic geography, to further emphasize our local roots. Some suggested keywords:
• volcano
• aurora borealis
• waterfall
• glacier

NB: the flyer will be printed out, therefore image resolution needs to be high enough to render nicely on paper.
The primary colors would be red, black and white – in line with our logo. But there is freedom to diverge and go for a different color scheme.

The logo should be present on the top front of the flyer. The URL www.brimvolt.com needs to be mentioned prominently, for example at the bottom of the page.

Examples of design we like:
• https://www.pixelbazaar.net/design/24252027
• https://www.pixelbazaar.net/design/24291120

Attached:
• the text for the brochure in PDF format
• our logo in vector format

IT, software, cybersecurity

EB3D1F
EC4F4E
F09395
F8D3D4
FCEDEE

• existing logo, and visuals related to computer, networks etc
• Icelandic geography/landscapes

```html
<!DOCTYPE html>
<html lang="en">
<head>
<meta charset="utf-8">
<title>Brimvolt – IT Services Flyer</title>
<link rel="stylesheet" href="https://fonts.googleapis.com/css2?family=Poppins:wght@400;500;600;700&display=swap">
<style>
:root{
  --red:#9b1b20;
  --red-deep:#761217;
  --black:#050505;
  --white:#ffffff;
  --stage:#ecebe8;
}
*{box-sizing:border-box;margin:0;padding:0}
html,body{width:1200px;height:873px;overflow:hidden;background:var(--stage);font-family:"Poppins",Arial,sans-serif}
.canvas{position:relative;width:1200px;height:873px}
.page{position:absolute;top:71px;width:468px;height:663px;overflow:hidden;background:var(--white);color:var(--white)}
.page--front{left:95px}
.page--back{left:621px;background:var(--black)}
.page svg.shapes{position:absolute;inset:0;width:468px;height:663px}
.brand{position:absolute;display:flex;align-items:center;gap:6px;font-weight:700;color:var(--red);letter-spacing:.5px}
.brand__dot{display:block;border:3px solid var(--red);border-radius:50%}
.front-brand{left:25px;top:16px;font-size:21px}
.front-brand .brand__dot{width:34px;height:34px}
.back-brand{left:78px;top:42px;font-size:21px}
.back-brand .brand__dot{width:32px;height:32px}
.seal-name{position:absolute;left:54px;top:150px;width:156px;text-align:center;font-weight:700;font-size:19px;color:var(--white);letter-spacing:1px}
.service{position:absolute;width:139px}
.service h2{font-size:8.8px;font-weight:700;line-height:1.3;text-transform:uppercase;color:var(--white);white-space:nowrap}
.service p{font-size:4.6px;line-height:1.45;text-align:justify;margin-top:9px;color:#f1f1f1}
.service--tight p{margin-top:4px}
.icon{position:absolute;width:34px;height:34px}
.contact{position:absolute;left:44px;top:496px;width:168px;text-align:center}
.contact h3{font-size:8.8px;font-weight:700;line-height:1.3;text-transform:uppercase;white-space:nowrap}
.contact .firm{font-size:7.4px;font-weight:400;margin-top:9px}
.contact-list{position:absolute;left:59px;top:573px;width:138px;list-style:none}
.contact-list li{display:flex;align-items:center;height:23px;padding-left:14px;font-size:7.4px;gap:8px;white-space:nowrap}
.contact-list li:first-child{margin-top:2px}
.contact-list svg{width:8px;height:8px;flex:none}
.site-url{position:absolute;left:212px;top:639px;width:256px;text-align:center;font-size:9px;font-weight:700;letter-spacing:5.2px;color:var(--black)}
</style>
</head>
<body>
<main class="canvas">

  <section class="page page--front">
    <svg class="shapes" viewBox="0 0 468 663">
      <defs>
        <radialGradient id="gradCoder" cx="45%" cy="50%" r="60%">
          <stop offset="0" stop-color="#d8c2a8"/>
          <stop offset=".45" stop-color="#3f5f86"/>
          <stop offset="1" stop-color="#0e1a33"/>
        </radialGradient>
        <radialGradient id="gradAnalyst" cx="55%" cy="55%" r="60%">
          <stop offset="0" stop-color="#5c84a3"/>
          <stop offset=".6" stop-color="#27465e"/>
          <stop offset="1" stop-color="#0f2031"/>
        </radialGradient>
      </defs>
      <rect x="0" y="262" width="468" height="372" fill="var(--black)"/>
      <rect x="0" y="630" width="468" height="33" fill="var(--white)"/>
      <circle cx="323" cy="151" r="160" fill="var(--white)"/>
      <circle cx="323" cy="151" r="153" fill="url(#gradCoder)" role="img" aria-label="Photo of a developer with headphones working at a laptop behind overlaid code"/>
      <circle cx="116" cy="323" r="121" fill="var(--white)"/>
      <circle cx="116" cy="323" r="114" fill="url(#gradAnalyst)" role="img" aria-label="Photo of a programmer in glasses looking at screens of code"/>
      <circle cx="132" cy="159" r="82" fill="var(--white)"/>
      <circle cx="132" cy="159" r="78" fill="var(--red)"/>
      <path d="M128 445 A91 91 0 0 1 219 536 V663" fill="none" stroke="var(--white)" stroke-width="1.5"/>
      <path d="M44 663 V536 A84 84 0 0 1 212 536 V663 Z" fill="var(--red)"/>
      <rect x="59" y="573" width="138" height="74" rx="5" fill="var(--red-deep)"/>
    </svg>

    <div class="brand front-brand"><span class="brand__dot"></span>BRIMVOLT</div>
    <div class="seal-name">BRIMVOLT</div>

    <svg class="icon" style="left:253px;top:337px" viewBox="0 0 34 34"><circle cx="17" cy="17" r="17" fill="var(--red)"/><rect x="10" y="13" width="14" height="10" rx="1.5" fill="none" stroke="#fff" stroke-width="1"/><path d="M14 13v-2h6v2M10 17h14" stroke="#fff" stroke-width="1" fill="none"/></svg>
    <article class="service" style="left:296px;top:349px">
      <h2>Brimvolt ehf – Your<br>Icelandic IT Partner</h2>
      <p>Step into a world of comprehensive IT solutions tailored to your unique needs. Our services, available on a contract or as-needed basis, are designed to empower your business and equip you with the tools you need to succeed. More than just a list of offerings, they’re a commitment to quality, a dedication to innovation, and a promise of reliability.</p>
    </article>

    <svg class="icon" style="left:253px;top:429px" viewBox="0 0 34 34"><circle cx="17" cy="17" r="17" fill="var(--red)"/><path d="M10 19l7 3.5 7-3.5M10 22l7 3.5 7-3.5M10 16l7-3.5 7 3.5-7 3.5z" fill="none" stroke="#fff" stroke-width="1"/><circle cx="17" cy="10" r="2" fill="none" stroke="#fff" stroke-width="1"/></svg>
    <article class="service" style="left:296px;top:440px">
      <h2>Software Development<br>and Integration Services</h2>
      <p>We specialize in custom software development across different platforms (desktop, server, embedded systems). We are open source software advocates, and leverage decades of experience to deliver innovative and cost-effective solutions tailored to your needs. Let’s build the perfect software solution for you.</p>
    </article>

    <svg class="icon" style="left:253px;top:517px" viewBox="0 0 34 34"><circle cx="17" cy="17" r="17" fill="var(--red)"/><circle cx="14" cy="15" r="4" fill="none" stroke="#fff" stroke-width="1.2" stroke-dasharray="2 1.2"/><circle cx="21" cy="21" r="3" fill="none" stroke="#fff" stroke-width="1.2" stroke-dasharray="1.6 1"/></svg>
    <article class="service" style="left:296px;top:530px">
      <h2>Systems Administration</h2>
      <p style="margin-top:18px">Are you having trouble with your IT infrastructure and in need of qualified personnel to take care of them? Or do you simply need a watchful and expert eye to ensure your systems keep running smoothly? We provide on-site and remote sysadmin services to manage your systems and bring you peace of mind. Take back control.</p>
    </article>

    <div class="contact">
      <h3>Get in touch with us<br>today to discuss<br>your IT needs in strict<br>confidence.</h3>
      <p class="firm">Brimvolt ehf</p>
    </div>
    <ul class="contact-list">
      <li><svg viewBox="0 0 8 8"><circle cx="4" cy="4" r="3.5" fill="#fff"/></svg>Website: www.brimvolt.com</li>
      <li><svg viewBox="0 0 8 8"><rect x=".5" y="1.5" width="7" height="5" fill="#fff"/><path d="M.5 1.5l3.5 3 3.5-3" stroke="var(--red-deep)" stroke-width=".8" fill="none"/></svg>E-mail: info@brimvolt.com</li>
      <li><svg viewBox="0 0 8 8"><path d="M1 1h2l1 2-1 1a5 5 0 0 0 1 1l1-1 2 1v2C4 7 1 4 1 1z" fill="#fff"/></svg>Phone: +354 555 0142</li>
    </ul>
    <p class="site-url">WWW.BRIMVOLT.COM</p>
  </section>

  <section class="page page--back">
    <svg class="shapes" viewBox="0 0 468 663">
      <defs>
        <linearGradient id="gradGlacier" x1="0" y1="0" x2="0" y2="1">
          <stop offset="0" stop-color="#3b4a6b"/>
          <stop offset=".3" stop-color="#b58aa0"/>
          <stop offset=".45" stop-color="#7fb2d6"/>
          <stop offset=".7" stop-color="#27344a"/>
          <stop offset="1" stop-color="#151d2a"/>
        </linearGradient>
      </defs>
      <circle cx="248" cy="4" r="318" fill="var(--red)"/>
      <circle cx="230" cy="13" r="311" fill="var(--white)"/>
      <circle cx="230" cy="13" r="304" fill="url(#gradGlacier)" role="img" aria-label="Photo of icebergs in a glacier lagoon at dusk under a pink sky"/>
      <circle cx="160" cy="55" r="111" fill="var(--red)"/>
      <circle cx="160" cy="55" r="105" fill="var(--white)"/>
      <rect x="0" y="630" width="468" height="33" fill="var(--white)"/>
      <path d="M128 445 A91 91 0 0 1 219 536 V663" fill="none" stroke="var(--white)" stroke-width="1.5"/>
      <path d="M44 663 V536 A84 84 0 0 1 212 536 V663 Z" fill="var(--red)"/>
      <rect x="59" y="573" width="138" height="74" rx="5" fill="var(--red-deep)"/>
    </svg>

    <div class="brand back-brand"><span class="brand__dot"></span>BRIMVOLT</div>

    <svg class="icon" style="left:38px;top:343px" viewBox="0 0 34 34"><circle cx="17" cy="17" r="17" fill="var(--red)"/><rect x="9" y="11" width="16" height="10" rx="1" fill="none" stroke="#fff" stroke-width="1"/><path d="M14 24h6M17 21v3" stroke="#fff" stroke-width="1"/></svg>
    <article class="service" style="left:82px;top:341px">
      <h2>Infrastructure<br>Monitoring Services</h2>
      <p>Do you know what is really going on inside your systems? We leverage leading open source monitoring solutions to bring visibility to your infrastructure. Monitor your systems proactively to ensure that they remain healthy at all times. Collect logs in real time and be notified when problems occur or warnings are raised. Fix issues before they become problems.</p>
    </article>

    <svg class="icon" style="left:244px;top:343px" viewBox="0 0 34 34"><circle cx="17" cy="17" r="17" fill="var(--red)"/><circle cx="14" cy="14" r="4" fill="none" stroke="#fff" stroke-width="1.2" stroke-dasharray="2 1.2"/><circle cx="21" cy="21" r="3.5" fill="none" stroke="#fff" stroke-width="1.2" stroke-dasharray="1.8 1"/></svg>
    <article class="service service--tight" style="left:288px;top:341px">
      <h2>Automation</h2>
      <p>Because you need effective tools to grow and prosper, it is essential that your IT systems align with your operational needs. We offer a comprehensive review of your business and IT environment so as to optimize the means already at your disposal. We streamline your workflow and develop new tools as needed, to make your IT systems work harder for you. Let us automate the boring stuff for you.</p>
    </article>

    <svg class="icon" style="left:244px;top:434px" viewBox="0 0 34 34"><circle cx="17" cy="17" r="17" fill="var(--red)"/><path d="M13 20a6 6 0 1 1 8 0v3h-8z" fill="none" stroke="#fff" stroke-width="1"/><path d="M14 25h6" stroke="#fff" stroke-width="1"/></svg>
    <article class="service service--tight" style="left:288px;top:432px">
      <h2>Technology Assessment<br>Services</h2>
      <p>Unsure about which tools are right for you or what IT strategy to pursue to help your business grow? We conduct market research and perform technical evaluations of software and hardware products to determine the best solutions for your company. Let’s empower your business with leading-edge solutions.</p>
    </article>

    <svg class="icon" style="left:244px;top:523px" viewBox="0 0 34 34"><circle cx="17" cy="17" r="17" fill="var(--red)"/><path d="M17 9l7 3v5c0 4-3 7-7 8-4-1-7-4-7-8v-5z" fill="none" stroke="#fff" stroke-width="1"/><path d="M14 17l2 2 4-4" fill="none" stroke="#fff" stroke-width="1"/></svg>
    <article class="service service--tight" style="left:288px;top:521px">
      <h2>Security Services</h2>
      <p>We understand the importance of security in today’s digital landscape. That’s why we offer comprehensive security services, including network audits to find and remedy flaws before they can be exploited to your disadvantage. We perform a thorough review of your IT environment to identify and remediate the weak spots, in order to keep your business secure, protect your assets and your reputation. Let’s raise your security posture to the highest standards, so that you don’t become the next victim – or headline. Bring the good guys in to keep the bad guys out.</p>
    </article>

    <div class="contact">
      <h3>Get in touch with us<br>today to discuss<br>your IT needs in strict<br>confidence.</h3>
      <p class="firm">Brimvolt ehf</p>
    </div>
    <ul class="contact-list">
      <li><svg viewBox="0 0 8 8"><circle cx="4" cy="4" r="3.5" fill="#fff"/></svg>Website: www.brimvolt.com</li>
      <li><svg viewBox="0 0 8 8"><rect x=".5" y="1.5" width="7" height="5" fill="#fff"/><path d="M.5 1.5l3.5 3 3.5-3" stroke="var(--red-deep)" stroke-width=".8" fill="none"/></svg>E-mail: info@brimvolt.com</li>
      <li><svg viewBox="0 0 8 8"><path d="M1 1h2l1 2-1 1a5 5 0 0 0 1 1l1-1 2 1v2C4 7 1 4 1 1z" fill="#fff"/></svg>Phone: +354 555 0142</li>
    </ul>
    <p class="site-url">WWW.BRIMVOLT.COM</p>
  </section>

</main>
</body>
</html>
```